We need a web design for a retail food business based in Greater Western Sydney Australia called Golden Lantern Chinese Restaurant. Basically just need a simple yet easily to navigate website to browse through a menu, gallery , brief description about us, opening hours.
Menu and Gallery will be constantly updated.
Will provide own images for gallery
Updates
Menu has been uploaded and some idea on the colours I would like on the site
Some additional pictures added to see what designs you guys can come up with . Thanks again
To All Designers,
Any extra fee on top of the designs that feels need to be charged, please let me know in advance
Reason: Extending Deadline as I have yet to find a design that I would like...Thanks guys
Target Market(s)
All groups
Industry/Entity Type
Business
Requirements
Must have
- Open minded to any designs
Nice to have
- Would like slideshow behind main logo.
Preferred light coloured site yet not too playful
Should not have
- Preferably no dark colours backgrounds

```html
<!DOCTYPE html>
<html lang="en">
<head>
<meta charset="utf-8">
<title>Golden Lantern Chinese Restaurant</title>
<link href="https://fonts.googleapis.com/css2?family=Roboto:wght@400;500&family=Roboto+Condensed:wght@400;700&family=Cabin+Condensed:wght@400;500&family=Federo&family=Oleo+Script&display=swap" rel="stylesheet">
<style>
:root{
  --red:#e2383c;
  --red-dark:#c3242a;
  --maroon:#7c1016;
  --cream:#fbe2a6;
  --grey:#555153;
  --panel:#ebe9e9;
  --white:#ffffff;
  --ink:#222222;
  --teal:#1fe0e0;
  --gold:#e6a935;
}
*{box-sizing:border-box;margin:0;padding:0}
html,body{width:942px;height:1200px;overflow:hidden;background:var(--white)}
body{font-family:"Roboto",sans-serif;color:var(--ink)}
.page{position:relative;width:942px;height:1200px;overflow:hidden;background:var(--grey)}
.abs{position:absolute}

/* header */
.topbar{left:0;top:0;width:942px;height:26px;background:var(--red-dark)}
.topbar .phone{left:126px;top:5px;color:var(--white);font:400 12px "Roboto Condensed",sans-serif;display:flex;align-items:center;gap:6px}
.header-band{left:0;top:26px;width:942px;height:65px;background:var(--red)}
.header-white{left:0;top:91px;width:942px;height:105px;background:var(--white);border-bottom:1px solid #ddd}
.brand{left:300px;top:32px;display:flex;align-items:center;gap:12px}
.brand .mark{width:58px;height:58px;border-radius:50%;background:var(--gold)}
.brand .name{font:700 27px/1.1 "Roboto Condensed",sans-serif;color:var(--white);text-transform:uppercase;letter-spacing:.5px}
.brand .name span{display:block}
.nav{left:0;top:163px;width:942px;height:22px}
.nav a{position:absolute;font:400 16px "Roboto Condensed",sans-serif;color:var(--ink);text-decoration:none}

/* hero */
.hero{left:0;top:196px;width:942px;height:308px;background:linear-gradient(100deg,#b98a32 0%,#e2c14a 30%,#d8a636 50%,#4a2c1c 70%,#8a5a38 100%)}
.dots{left:676px;top:474px;display:flex;gap:6px}
.dots i{display:block;width:15px;height:15px;border-radius:50%;background:var(--white)}
.dots i.on{background:var(--teal)}

/* offer */
.strip{left:0;top:504px;width:942px;height:19px;background:var(--white);border-top:4px solid #f6c9c6}
.offer{left:0;top:523px;width:942px;height:115px;background:var(--red)}
.ribbon{left:192px;top:518px;width:71px;height:106px}
.ribbon-label{left:196px;top:533px;width:63px;font:400 14px/20px "Oleo Script",cursive;color:var(--white);text-align:center}
.offer-title{left:282px;top:532px;font:400 26px "Federo",sans-serif;color:var(--white);letter-spacing:1px}
.offer-list{left:285px;top:570px;list-style:none;color:var(--white);font:400 13px "Roboto",sans-serif}
.offer-list li{height:24px;display:flex;align-items:center;gap:7px}
.btn-offer{left:645px;top:575px;width:96px;height:45px;background:var(--cream);border-radius:5px;color:var(--red-dark);font:400 18px "Roboto Condensed",sans-serif;display:flex;align-items:center;justify-content:center;box-shadow:1px 2px 3px rgba(0,0,0,.35)}

/* side tabs */
.tab{left:0;width:86px;background:var(--red);color:var(--white);font:500 12px/1.2 "Roboto",sans-serif;text-align:center;border-radius:0 4px 4px 0;box-shadow:2px 2px 3px rgba(0,0,0,.4);display:flex;flex-direction:column;align-items:center;justify-content:center}
.tab.lunch{top:708px;height:38px}
.tab.takeaway{top:759px;height:38px}
.tab.quick{top:883px;height:79px;gap:3px;font-weight:400}
.tab.quick .icon{width:40px;height:40px;border-radius:50%;background:var(--white);display:flex;align-items:center;justify-content:center}

/* main column */
.h2{font:400 22px "Cabin Condensed",sans-serif;color:var(--white)}
.special-title{left:191px;top:667px}
.special-photo{left:192px;top:707px;width:348px;height:158px;background:linear-gradient(120deg,#e9d7a8 0%,#e58a2a 30%,#c4451e 55%,#e2b04a 80%,#9bb56a 100%)}
.dish-name{left:192px;top:879px;font:400 14px "Roboto Condensed",sans-serif;color:var(--cream)}
.dish-desc{left:192px;top:899px;width:340px;font:400 11px/1.35 "Roboto",sans-serif;color:var(--white)}
.btn-small{left:467px;top:931px;width:51px;height:22px;background:var(--red);color:var(--white);font:400 9px "Roboto",sans-serif;display:flex;align-items:center;justify-content:center}
.gallery-title{left:191px;top:974px;border-bottom:1px solid var(--white);width:215px;padding-bottom:1px}
.thumb{top:1014px;width:75px;height:74px;border:2px solid var(--white)}
.t1{left:195px;background:linear-gradient(135deg,#6a1a10,#b24a2a)}
.t2{left:285px;background:linear-gradient(135deg,#3a2418,#b06a30)}
.t3{left:376px;background:linear-gradient(135deg,#f1e3b0,#d49a3a)}
.t4{left:465px;background:linear-gradient(135deg,#f3f3f3,#8a1a1a)}
.arrow{top:1042px}

/* sidebar */
.sidebar{left:572px;top:664px;width:176px;height:441px;background:var(--panel);border:1px solid #cfcfcf}
.side-head{position:absolute;left:4px;width:168px;height:24px;background:var(--red);border-left:5px solid #222;color:var(--white);font:400 14px "Cabin Condensed",sans-serif;padding-left:7px;line-height:24px}
.hours-head{top:6px}
.recipe-head{top:297px}
.sub{position:absolute;left:6px;font:400 12px "Roboto Condensed",sans-serif;color:var(--ink);text-decoration:underline}
.row{position:absolute;left:6px;width:166px;height:20px;font:400 11px "Roboto Condensed",sans-serif;color:#444;display:flex;align-items:center;border-bottom:1px solid #d8d8d8}
.row .day{width:71px}
.row .time{display:flex;align-items:center;gap:4px;color:var(--ink)}
.row.lunch-row{border:none;color:var(--ink)}
.row.lunch-row .day{width:87px}
.divider{position:absolute;left:8px;top:282px;width:160px;border-top:1px dashed #8a8ab0}
.recipes{position:absolute;left:15px;top:333px;list-style:none}
.recipes li{height:16.6px;font:400 11px "Roboto",sans-serif;color:var(--ink);display:flex;align-items:center;gap:5px;text-transform:uppercase;letter-spacing:.3px}
.recipes li::before{content:"";width:4px;height:4px;border-right:1.5px solid var(--red);border-top:1.5px solid var(--red);transform:rotate(45deg)}

/* footer */
.footer{left:0;top:1119px;width:942px;height:81px;background:var(--red)}
.footer-links{left:179px;top:1135px;display:flex;gap:20px}
.footer-links a{color:var(--white);font:400 12px "Roboto",sans-serif;text-decoration:none;border-bottom:1px dotted var(--white);display:flex;align-items:center;gap:8px}
.social{left:589px;top:1128px;display:flex;gap:7px}
.social i{display:block;width:30px;height:30px;border-radius:5px}
.social .s1{background:#3b5b9c}.social .s2{background:#2aa7df}.social .s3{background:#c61d24}.social .s4{background:#f07b1b}
.copyright{left:0;top:1181px;width:942px;text-align:center;color:var(--white);font:400 11px "Roboto",sans-serif}
</style>
</head>
<body>
<div class="page">

  <header>
    <div class="abs topbar">
      <div class="abs phone">
        <svg width="16" height="16" viewBox="0 0 24 24"><path fill="#fff" d="M6.6 10.8a15.1 15.1 0 0 0 6.6 6.6l2.2-2.2c.3-.3.7-.4 1-.2 1.1.4 2.3.6 3.6.6.6 0 1 .4 1 1V20c0 .6-.4 1-1 1A17 17 0 0 1 3 4c0-.6.4-1 1-1h3.5c.6 0 1 .4 1 1 0 1.3.2 2.5.6 3.6.1.3 0 .7-.2 1z"/></svg>
        Make a Reservation : (02) 5550 1287
      </div>
    </div>
    <div class="abs header-band"></div>
    <div class="abs header-white"></div>
    <div class="abs brand">
      <div class="mark"></div>
      <div class="name">Golden Lantern<span>Chinese Restaurant</span></div>
    </div>
    <nav class="abs nav">
      <a style="left:235px">Home</a>
      <a style="left:329px">Menu</a>
      <a style="left:424px">Gallery</a>
      <a style="left:518px">Contact</a>
      <a style="left:617px">Reservations</a>
    </nav>
  </header>

  <section>
    <div class="abs hero" role="img" aria-label="Slideshow photo of the restaurant dining room and bar"></div>
    <div class="abs dots"><i class="on"></i><i></i><i></i><i></i></div>
  </section>

  <section>
    <div class="abs strip"></div>
    <div class="abs offer"></div>
    <svg class="abs ribbon" viewBox="0 0 71 106"><path d="M0 0H71V106L35.5 84 0 106Z" fill="#8e1419"/><path d="M5 4H66V96L35.5 78 5 96Z" fill="none" stroke="#e7b7b7" stroke-width="1"/></svg>
    <div class="abs ribbon-label">Special<br>Offers</div>
    <h2 class="abs offer-title">Special Offer Of The Month</h2>
    <ul class="abs offer-list">
      <li><svg width="12" height="12" viewBox="0 0 12 12"><circle cx="6" cy="6" r="3" fill="none" stroke="#fff" stroke-width="1.4"/><path d="M6 0v2M6 10v2M0 6h2M10 6h2M1.8 1.8l1.4 1.4M8.8 8.8l1.4 1.4M1.8 10.2l1.4-1.4M8.8 3.2l1.4-1.4" stroke="#fff" stroke-width="1.2"/></svg>Order over $22, receive 6 mini rolls or 6 chicken wings</li>
      <li><svg width="12" height="12" viewBox="0 0 12 12"><circle cx="6" cy="6" r="3" fill="none" stroke="#fff" stroke-width="1.4"/><path d="M6 0v2M6 10v2M0 6h2M10 6h2M1.8 1.8l1.4 1.4M8.8 8.8l1.4 1.4M1.8 10.2l1.4-1.4M8.8 3.2l1.4-1.4" stroke="#fff" stroke-width="1.2"/></svg>Order over $40, receive any dish to the value of $10.</li>
    </ul>
    <a class="abs btn-offer">Read More</a>
  </section>

  <aside>
    <a class="abs tab lunch">Bussiness<br>lunch</a>
    <a class="abs tab takeaway">Take Away<br>Menu</a>
    <a class="abs tab quick">
      <span class="icon"><svg width="20" height="24" viewBox="0 0 20 24"><rect x="1" y="1" width="18" height="22" rx="2" fill="#e6a935"/><path d="M5 8h10M5 12h10M5 16h10" stroke="#fff" stroke-width="1.5"/></svg></span>
      Quick<br>Reservation
    </a>
  </aside>

  <main>
    <h2 class="abs h2 special-title">Speciality of the House</h2>
    <div class="abs special-photo" role="img" aria-label="Photo of Mee Korb crispy noodles with prawns"></div>
    <h3 class="abs dish-name">Mee Korb (Thai)</h3>
    <p class="abs dish-desc">Crispy deep fried rice vermicelli with prawns,pork, bean sprouts, tossed with a Thai style spicy sauce.</p>
    <a class="abs btn-small">Read More</a>

    <h2 class="abs h2 gallery-title">Restaurant Photo Gallery</h2>
    <svg class="abs arrow" style="left:177px" width="12" height="18" viewBox="0 0 12 18"><path d="M10 2 3 9l7 7" fill="none" stroke="#aaa" stroke-width="3"/></svg>
    <div class="abs thumb t1" role="img" aria-label="Gallery photo of a glazed meat dish"></div>
    <div class="abs thumb t2" role="img" aria-label="Gallery photo of a sizzling plate"></div>
    <div class="abs thumb t3" role="img" aria-label="Gallery photo of a noodle soup"></div>
    <div class="abs thumb t4" role="img" aria-label="Gallery photo of honey ribs"></div>
    <svg class="abs arrow" style="left:544px" width="12" height="18" viewBox="0 0 12 18"><path d="M2 2l7 7-7 7" fill="none" stroke="#aaa" stroke-width="3"/></svg>
  </main>

  <aside class="abs sidebar">
    <h3 class="side-head hours-head">Opening Hours</h3>
    <span class="sub" style="top:37px">LUNCH</span>
    <div class="row lunch-row" style="top:53px"><span class="day">Monday- Friday</span><span class="time">11:30am - 3:00pm</span></div>
    <span class="sub" style="top:81px">DINNER</span>
    <div class="row" style="top:97px"><span class="day">Monday</span><span class="time"><svg width="12" height="12" viewBox="0 0 12 12"><circle cx="6" cy="6" r="5" fill="none" stroke="#222"/><path d="M6 3v3h2.5" fill="none" stroke="#222"/></svg>5:00pm - 9:30pm</span></div>
    <div class="row" style="top:120px"><span class="day">Tuesday</span><span class="time"><svg width="12" height="12" viewBox="0 0 12 12"><circle cx="6" cy="6" r="5" fill="none" stroke="#222"/><path d="M6 3v3h2.5" fill="none" stroke="#222"/></svg>5:00pm - 9:30pm</span></div>
    <div class="row" style="top:143px"><span class="day">Wednesday</span><span class="time"><svg width="12" height="12" viewBox="0 0 12 12"><circle cx="6" cy="6" r="5" fill="none" stroke="#222"/><path d="M6 3v3h2.5" fill="none" stroke="#222"/></svg>5:00pm - 9:30pm</span></div>
    <div class="row" style="top:165px"><span class="day">Thursday</span><span class="time"><svg width="12" height="12" viewBox="0 0 12 12"><circle cx="6" cy="6" r="5" fill="none" stroke="#222"/><path d="M6 3v3h2.5" fill="none" stroke="#222"/></svg>5:00pm - 9:30pm</span></div>
    <div class="row" style="top:187px"><span class="day">Friday</span><span class="time"><svg width="12" height="12" viewBox="0 0 12 12"><circle cx="6" cy="6" r="5" fill="none" stroke="#222"/><path d="M6 3v3h2.5" fill="none" stroke="#222"/></svg>5:00pm - 10:30pm</span></div>
    <div class="row" style="top:210px"><span class="day">Saturday</span><span class="time"><svg width="12" height="12" viewBox="0 0 12 12"><circle cx="6" cy="6" r="5" fill="none" stroke="#222"/><path d="M6 3v3h2.5" fill="none" stroke="#222"/></svg>5:00pm - 10:30pm</span></div>
    <div class="row" style="top:231px"><span class="day">Sunday</span><span class="time"><svg width="12" height="12" viewBox="0 0 12 12"><circle cx="6" cy="6" r="5" fill="none" stroke="#222"/><path d="M6 3v3h2.5" fill="none" stroke="#222"/></svg>5:00pm - 10:30pm</span></div>
    <div class="row" style="top:254px;border:none"><span class="day">Public Holiday</span><span class="time"><svg width="12" height="12" viewBox="0 0 12 12"><circle cx="6" cy="6" r="5" fill="none" stroke="#222"/><path d="M6 3v3h2.5" fill="none" stroke="#222"/></svg>5:00pm - 9:30pm</span></div>
    <div class="divider"></div>

    <h3 class="side-head recipe-head">Mouth-Watering Recipes</h3>
    <ul class="recipes" style="top:333px">
      <li>Orange Honey Ribs</li>
      <li>Seafood Supreme</li>
      <li>Soya Soft Noodles</li>
      <li>Mee Korb (Thai)</li>
      <li>Mongolian Lamb</li>
      <li>Shun Tung Chicken</li>
    </ul>
  </aside>

  <footer>
    <div class="abs footer"></div>
    <div class="abs footer-links">
      <a><svg width="6" height="9" viewBox="0 0 6 9"><path d="M1 1l3.5 3.5L1 8" fill="none" stroke="#fff" stroke-width="1.6"/></svg>Contact Us</a>
      <a><svg width="6" height="9" viewBox="0 0 6 9"><path d="M1 1l3.5 3.5L1 8" fill="none" stroke="#fff" stroke-width="1.6"/></svg>About Us</a>
    </div>
    <div class="abs social"><i class="s1"></i><i class="s2"></i><i class="s3"></i><i class="s4"></i></div>
    <p class="abs copyright">Copyright © 2013, GoldenLantern.com, All Rights Reserved.</p>
  </footer>

</div>
</body>
</html>
```